New Business and Accounting Software need a Web Site

The website is for a Business and Accounting Software that has 8 products.
Each product has its owns logo and color, when you do the design have in consideration that we are looking the experience that when you change from one product page to another the look and feel adjust to the color and logo of the product.
The product are:
Ventas (Sales)
Compras (Purchases)
Contabilidad (Accounting)
Presupuesto (Budget)
Inventarios (Inventory)
Bancos (Banks)
NĂ³mina RH (Human Resources Payroll)
CRM (Customer Relationship Manager)

You can see how the main logo and variations are used in each page
- https://www.ufta.com/
- https://www.vemi.com/
- https://www.prulvin.com/

Our goal is to be similar to them.

I have created a word document to explain what I want.
You need to design:
1 Home Page
1 Product Landing Page
1 Product Detail Page
1 Price Page

I am attaching:
1. Main Logo
2. 8 Product Logos
3. Website Idea, you can create your own idea.

You are welcome to use other icons for the each product if you want.

Target Market(s)

Independet professionals and Small and Medium Companies

Industry/Entity Type

Business and Accounting Software

Coding

Coded - Design and coding required

Colors
0054AA
0677BA
7BADD7
CADEEF
E8F1F8

Requirements
Must have
• Must show all products in the main page

```html
<!DOCTYPE html>
<html lang="en">
<head>
<meta charset="UTF-8">
<title>nexa.cr — Business and Accounting Software</title>
<link href="https://fonts.googleapis.com/css2?family=Poppins:wght@500;600;700&family=Roboto:wght@400;500;700&display=swap" rel="stylesheet">
<style>
:root{
  --blue-900:#0054AA;
  --blue-700:#0677BA;
  --blue-400:#7BADD7;
  --blue-200:#CADEEF;
  --blue-100:#E8F1F8;
  --ink:#111111;
  --muted:#555d66;
  --white:#ffffff;
}
*{box-sizing:border-box;margin:0;padding:0}
html,body{width:1200px;height:3185px;overflow:hidden}
body{font-family:'Roboto',sans-serif;color:var(--ink);background:var(--white);position:relative}
.abs{position:absolute}
.btn{position:absolute;display:flex;align-items:center;justify-content:center;gap:10px;font:700 13px 'Roboto',sans-serif;text-transform:uppercase;color:var(--white);background:var(--blue-900);border-radius:3px;letter-spacing:.2px;z-index:2}
.btn .dot{width:12px;height:12px;border-radius:50%;background:currentColor;position:relative}
.btn .dot::after{content:"";position:absolute;left:3px;top:3px;border-left:5px solid var(--blue-900);border-top:3px solid transparent;border-bottom:3px solid transparent}
.btn.light{background:var(--blue-400)}
.btn.light .dot::after{border-left-color:var(--blue-400)}
.btn.outline{background:transparent;border:2px solid var(--white)}
.btn.outline .dot::after{border-left-color:var(--blue-900)}

/* header */
.site-header{position:absolute;left:0;top:0;width:1200px;height:90px;background:var(--white);z-index:3}
.brand{position:absolute;display:flex;align-items:center;gap:10px;font-family:'Poppins',sans-serif;font-weight:700;color:var(--blue-900)}
.brand .mark{border-radius:50%;background:var(--blue-900)}
.site-header .brand{left:112px;top:14px;font-size:44px}
.site-header .brand .mark{width:22px;height:22px}
.nav{position:absolute;top:36px;left:400px;display:flex;gap:27px;font:500 15px 'Roboto',sans-serif}
.nav .active{color:var(--blue-900)}
.lang{position:absolute;left:860px;top:34px;font:500 14px 'Roboto',sans-serif;display:flex;align-items:center;gap:8px}
.lang .flag{width:22px;height:22px;border-radius:50%;background:var(--blue-200)}
.login{left:972px;top:25px;width:116px;height:42px}

/* hero */
.hero{position:absolute;left:0;top:90px;width:1200px;height:790px;background:linear-gradient(180deg,#f1f6fb,#eaf2fa);overflow:hidden}
.hero-welcome{left:112px;top:122px;font:700 26px/1.2 'Poppins',sans-serif;z-index:2}
.hero-title{left:106px;top:154px;font:700 112px/1.1 'Poppins',sans-serif;color:var(--blue-900);letter-spacing:-1px;z-index:2}
.hero-text{left:112px;top:296px;width:480px;font:500 15px/24px 'Roboto',sans-serif;z-index:2}

/* product grid */
.tiles{position:absolute;left:112px;top:910px;width:976px;height:420px;display:grid;grid-template-columns:repeat(4,1fr);grid-template-rows:repeat(2,1fr)}
.tile{position:relative;display:flex;flex-direction:column;align-items:center;justify-content:flex-end;padding-bottom:22px;color:var(--white);font:500 26px 'Roboto',sans-serif}
.tile .badge{position:absolute;top:38px;left:50%;transform:translateX(-50%);width:100px;height:100px;border-radius:50%;background:rgba(255,255,255,.22)}
.t-ventas{background:linear-gradient(180deg,#DC8B55,#FBA82A)}
.t-compras{background:linear-gradient(180deg,#0C5DB4,#7BB5EE)}
.t-conta{background:linear-gradient(180deg,#D8708F,#C56BD8)}
.t-presu{background:linear-gradient(180deg,#26918F,#27C48E)}
.t-inv{background:linear-gradient(180deg,#A65A5F,#E35566)}
.t-bancos{background:linear-gradient(180deg,#555,#9c9c9c)}
.t-nomina{background:linear-gradient(180deg,#79B58D,#77CFCB)}
.t-crm{background:linear-gradient(180deg,#6E78A6,#7672DC)}

/* products section */
.products{position:absolute;left:0;top:1428px;width:1200px;height:694px;background:var(--blue-100);overflow:hidden}
.section-title{position:absolute;left:0;width:1200px;text-align:center;font:700 30px 'Poppins',sans-serif;color:var(--blue-900)}
.tabs{position:absolute;left:112px;top:127px;display:flex;gap:6px}
.tab{width:117px;height:43px;border:1px solid var(--blue-900);background:var(--white);color:var(--blue-900);font:700 13px 'Roboto',sans-serif;display:flex;align-items:center;justify-content:center}
.tab.active{background:var(--blue-900);color:var(--white)}
.product-name{left:112px;top:222px;font:700 38px 'Poppins',sans-serif;color:var(--blue-900)}
.product-rule{left:112px;top:279px;width:40px;height:3px;background:var(--blue-900)}
.features{position:absolute;left:112px;top:300px;list-style:none}
.features li{height:39.5px;display:flex;align-items:center;gap:22px;font:400 16px 'Roboto',sans-serif;color:var(--muted)}
.features li svg{flex:none}

/* why */
.card{position:absolute;top:2268px;width:235px;height:220px;border-radius:18px;background:var(--blue-900);color:var(--white);text-align:center;padding:0 14px}
.card .num{margin-top:24px;font:700 44px 'Poppins',sans-serif}
.card h3{margin-top:4px;font:700 19px 'Roboto',sans-serif}
.card p{margin-top:8px;font:400 14px/21px 'Roboto',sans-serif;color:#dfeaf6}

/* cta */
.cta{position:absolute;left:0;top:2605px;width:1200px;height:408px;background:linear-gradient(135deg,#0a5db6,var(--blue-900));overflow:hidden}
.cta-text{left:645px;top:80px;width:460px;font:700 31px/39px 'Poppins',sans-serif;color:var(--blue-200)}

/* footer */
.site-footer .brand{left:112px;top:3058px;font-size:56px}
.site-footer .brand .mark{width:26px;height:26px}
.copyright{left:488px;top:3091px;font:400 15px 'Roboto',sans-serif;color:#444}
</style>
</head>
<body>

<header class="site-header">
  <div class="brand"><span>nexa.cr</span><span class="mark"></span></div>
  <nav class="nav">
    <span class="active">Home</span><span>Our Products</span><span>Solutions</span><span>Plans</span><span>Contact Us</span>
  </nav>
  <div class="lang"><span class="flag"></span>Eng
    <svg width="10" height="6" viewBox="0 0 10 6"><path d="M0 0h10L5 6z" fill="#111"/></svg>
  </div>
  <a class="btn login">Log in
    <svg width="10" height="12" viewBox="0 0 10 12"><rect x="0" y="5" width="10" height="7" rx="1" fill="#fff"/><path d="M2.5 5V3.5a2.5 2.5 0 015 0V5" stroke="#fff" stroke-width="1.6" fill="none"/></svg>
  </a>
</header>

<section class="hero">
  <svg class="abs" style="left:0;top:0" width="1200" height="790" viewBox="0 0 1200 790">
    <circle cx="800" cy="250" r="202" fill="var(--blue-900)"/>
    <circle cx="800" cy="250" r="90" fill="#eef4fa"/>
    <polygon points="0,505 340,688 1200,455 1200,540 340,770 0,585" fill="var(--blue-400)"/>
  </svg>
  <div class="abs hero-welcome">Welcome To</div>
  <div class="abs hero-title">Nexa cr</div>
  <p class="abs hero-text">Lorem ipsum dolor sit amet, consectetur adipiscing elit, sed do eiusmod tempor incididunt ut labore et dolore</p>
  <a class="btn" style="left:112px;top:370px;width:153px;height:50px">Free Trial <span class="dot"></span></a>
  <a class="btn light" style="left:280px;top:370px;width:152px;height:50px">Get Started <span class="dot"></span></a>
  <div class="abs" role="img" aria-label="Desktop monitor showing the invoicing screen of the software" style="left:622px;top:100px;width:530px;height:490px;border-radius:14px;background:linear-gradient(160deg,#e9edf2,#c9d0d8)"></div>
</section>

<div class="tiles">
  <div class="tile t-ventas"><span class="badge"></span>Ventas</div>
  <div class="tile t-compras"><span class="badge"></span>Compras</div>
  <div class="tile t-conta"><span class="badge"></span>Contabilidad</div>
  <div class="tile t-presu"><span class="badge"></span>Presupuesto</div>
  <div class="tile t-inv"><span class="badge"></span>Inventarios</div>
  <div class="tile t-bancos"><span class="badge"></span>Bancos</div>
  <div class="tile t-nomina"><span class="badge"></span>Nómina RH</div>
  <div class="tile t-crm"><span class="badge"></span>CRM</div>
</div>

<section class="products">
  <svg class="abs" style="left:0;top:0" width="1200" height="694" viewBox="0 0 1200 694">
    <defs><linearGradient id="org" x1="0" y1="0" x2="0" y2="1"><stop offset="0" stop-color="#D9875A"/><stop offset="1" stop-color="#FBA825"/></linearGradient></defs>
    <circle cx="1140" cy="429" r="212" fill="url(#org)"/>
  </svg>
  <h2 class="section-title" style="top:54px">Our Products</h2>
  <div class="tabs">
    <div class="tab active">VENTAS</div><div class="tab">COMPRAS</div><div class="tab">CONTABILIDAD</div><div class="tab">PRESUPUESTO</div>
    <div class="tab">INVENTARIOS</div><div class="tab">BANCOS</div><div class="tab">NÓMINA RH</div><div class="tab">CRM</div>
  </div>
  <div class="abs product-name">Ventas</div>
  <div class="abs product-rule"></div>
  <ul class="features">
    <li><svg width="14" height="14" viewBox="0 0 14 14"><circle cx="7" cy="7" r="7" fill="var(--blue-900)"/><path d="M3.8 7.2l2.2 2.2 4.2-4.4" stroke="#fff" stroke-width="1.8" fill="none"/></svg>Lorem ipsum dolor sit amet, consectetur adipiscing elit</li>
    <li><svg width="14" height="14" viewBox="0 0 14 14"><circle cx="7" cy="7" r="7" fill="var(--blue-900)"/><path d="M3.8 7.2l2.2 2.2 4.2-4.4" stroke="#fff" stroke-width="1.8" fill="none"/></svg>Lorem ipsum dolor sit amet, consectetur adipiscing elit</li>
    <li><svg width="14" height="14" viewBox="0 0 14 14"><circle cx="7" cy="7" r="7" fill="var(--blue-900)"/><path d="M3.8 7.2l2.2 2.2 4.2-4.4" stroke="#fff" stroke-width="1.8" fill="none"/></svg>Lorem ipsum dolor sit amet, consectetur adipiscing elit</li>
    <li><svg width="14" height="14" viewBox="0 0 14 14"><circle cx="7" cy="7" r="7" fill="var(--blue-900)"/><path d="M3.8 7.2l2.2 2.2 4.2-4.4" stroke="#fff" stroke-width="1.8" fill="none"/></svg>Lorem ipsum dolor sit amet, consectetur adipiscing elit</li>
    <li><svg width="14" height="14" viewBox="0 0 14 14"><circle cx="7" cy="7" r="7" fill="var(--blue-900)"/><path d="M3.8 7.2l2.2 2.2 4.2-4.4" stroke="#fff" stroke-width="1.8" fill="none"/></svg>Lorem ipsum dolor sit amet, consectetur adipiscing elit</li>
    <li><svg width="14" height="14" viewBox="0 0 14 14"><circle cx="7" cy="7" r="7" fill="var(--blue-900)"/><path d="M3.8 7.2l2.2 2.2 4.2-4.4" stroke="#fff" stroke-width="1.8" fill="none"/></svg>Lorem ipsum dolor sit amet, consectetur adipiscing elit</li>
    <li><svg width="14" height="14" viewBox="0 0 14 14"><circle cx="7" cy="7" r="7" fill="var(--blue-900)"/><path d="M3.8 7.2l2.2 2.2 4.2-4.4" stroke="#fff" stroke-width="1.8" fill="none"/></svg>Lorem ipsum dolor sit amet, consectetur adipiscing elit</li>
  </ul>
  <a class="btn" style="left:112px;top:589px;width:153px;height:50px">Learn More <span class="dot"></span></a>
  <div class="abs" role="img" aria-label="Sales module screen with the customer list" style="left:610px;top:307px;width:532px;height:255px;background:linear-gradient(180deg,#f4f5f7,#e6e8eb);border-top:8px solid var(--blue-900);border-bottom:4px solid var(--blue-900);box-shadow:0 6px 18px rgba(0,0,0,.15)"></div>
</section>

<h2 class="section-title" style="top:2186px">Why Choose Us</h2>
<div class="card" style="left:107px"><div class="num">01</div><h3>Lorem Ipsum Dolor</h3><p>Sed ut perspiciatis unde omnis iste natus error sit voluptatem accusantium</p></div>
<div class="card" style="left:357px"><div class="num">02</div><h3>Lorem Ipsum Dolor</h3><p>Sed ut perspiciatis unde omnis iste natus error sit voluptatem accusantium</p></div>
<div class="card" style="left:607px"><div class="num">03</div><h3>Lorem Ipsum Dolor</h3><p>Sed ut perspiciatis unde omnis iste natus error sit voluptatem accusantium</p></div>
<div class="card" style="left:857px"><div class="num">04</div><h3>Lorem Ipsum Dolor</h3><p>Sed ut perspiciatis unde omnis iste natus error sit voluptatem accusantium</p></div>

<section class="cta">
  <div class="abs" role="img" aria-label="Man with glasses working on a laptop" style="left:145px;top:0;width:408px;height:408px;border-radius:50% 50% 0 0;background:linear-gradient(180deg,#f2f2f2,#cfd6dd)"></div>
  <p class="abs cta-text">Lorem ipsum dolor sit amet consectetur adipiscing elit sed do eiusmod tempor inci didunt</p>
  <a class="btn outline" style="left:645px;top:267px;width:153px;height:50px">Learn More <span class="dot"></span></a>
</section>

<footer class="site-footer">
  <div class="brand"><span>nexa.cr</span><span class="mark"></span></div>
  <div class="abs copyright">© 2022 Nexa. All Rights Reserved</div>
  <a class="btn" style="left:917px;top:3073px;width:170px;height:50px">Subscribe Now <span class="dot"></span></a>
</footer>

</body>
</html>
```